Global social media analytics company needs business card design

We need an updated business card design to align with our new website - brightquillo.net -

I would also like a favicon designed as well.

Target Market(s)

CEOs, CMOs go big companies

Industry/Entity Type

Business

Contact Information for Business Card

Room for the following:
Address
Main telephone
Direct telephone or cell phone
twitter handle

Colors
aaaaaa

Requirements
Must have
• Attention to detail; style.
• Use the logo color from our website - which is gray

```html
<!DOCTYPE html>
<html lang="en">
<head>
<meta charset="utf-8">
<title>brightquillo business card</title>
<link href="https://fonts.googleapis.com/css2?family=Questrial&display=swap" rel="stylesheet">
<style>
  :root {
    --page: #ffffff;
    --card-front: #a9a9a9;
    --card-back: #3f4040;
    --mark-dark: #3c3d3d;
    --ink-light: #ffffff;
    --ink-soft: #e6e6e6;
    --ghost: #4a4b4b;
  }
  * { margin: 0; padding: 0; box-sizing: border-box; }
  html, body {
    width: 1200px; height: 1000px; overflow: hidden;
    background: var(--page);
    font-family: "Questrial", "Century Gothic", sans-serif;
  }
  .card {
    position: absolute;
    left: 244px;
    width: 712px; height: 416px;
    overflow: hidden;
  }
  .card--front { top: 60px; background: var(--card-front); }
  .card--back { top: 520px; background: var(--card-back); }

  .brand {
    position: absolute;
    display: flex; align-items: center;
  }
  .brand__dot { border-radius: 50%; flex: none; }
  .brand__name { font-weight: 400; letter-spacing: -0.5px; line-height: 1; }

  .card--front .brand { left: 142px; top: 154px; }
  .card--front .brand__dot { width: 108px; height: 108px; background: var(--mark-dark); margin-right: 18px; }
  .card--front .brand__name { font-size: 46px; color: var(--mark-dark); }

  .card--back .brand { left: 62px; top: 84px; }
  .card--back .brand__dot { width: 68px; height: 68px; background: var(--ink-light); margin-right: 12px; }
  .card--back .brand__name { font-size: 30px; color: var(--ink-light); }

  .ghost-mark {
    position: absolute; left: 80px; bottom: 34px;
    display: flex; align-items: center;
  }
  .ghost-mark__dot { width: 150px; height: 150px; border-radius: 50%; background: var(--ghost); margin-right: 20px; }
  .ghost-mark__name { font-size: 92px; color: var(--ghost); letter-spacing: -1px; line-height: 1; }

  .contact { position: absolute; left: 96px; top: 200px; color: var(--ink-soft); }
  .contact__name { font-size: 19px; color: var(--ink-light); font-weight: 700; margin-left: -4px; margin-bottom: 22px; }
  .contact__line { display: flex; align-items: center; font-size: 17px; height: 26px; }
  .contact__icon { width: 20px; height: 16px; margin-right: 10px; fill: var(--ink-light); }
</style>
</head>
<body>
  <section class="card card--front">
    <div class="brand">
      <span class="brand__dot"></span>
      <span class="brand__name">brightquillo</span>
    </div>
  </section>

  <section class="card card--back">
    <div class="ghost-mark" aria-hidden="true">
      <span class="ghost-mark__dot"></span>
      <span class="ghost-mark__name">brightquillo</span>
    </div>

    <div class="brand">
      <span class="brand__dot"></span>
      <span class="brand__name">brightquillo</span>
    </div>

    <div class="contact">
      <p class="contact__name">Name Surname</p>
      <p class="contact__line">
        <svg class="contact__icon" viewBox="0 0 20 16"><path d="M2 5 Q10 -1 18 5 L16 7 L13 5.5 L13 4 Q10 3 7 4 L7 5.5 L4 7 Z"/><rect x="4" y="8" width="12" height="7" rx="1.5"/></svg>
        000 0000
      </p>
      <p class="contact__line">
        <svg class="contact__icon" viewBox="0 0 20 16"><path d="M1 2 H19 V14 H1 Z M2.5 3.5 L10 9 L17.5 3.5" fill="none" stroke="#fff" stroke-width="1.8"/></svg>
        email@quillmail.net.au
      </p>
      <p class="contact__line">
        <svg class="contact__icon" viewBox="0 0 20 16"><path d="M10 0 A5 5 0 0 1 15 5 C15 9 10 16 10 16 C10 16 5 9 5 5 A5 5 0 0 1 10 0 Z M10 3 A2 2 0 1 0 10 7 A2 2 0 1 0 10 3 Z" fill-rule="evenodd"/></svg>
        PO Box 0000 Harrowdale WA 6000
      </p>
    </div>
  </section>
</body>
</html>
```